Black Granite Web Design Project

We are looking for a design for a new company that will be selling Black Granite slabs and tiles. We will be selling to both end-consumers and granite installers. We have already settled on a logo and hopefully this will give an idea of what we like in our designs. We are not going to be selling online but want people to call us so the site is basically an enhanced business card. We will be focusing a lot on SEO so the design will have to keep that in mind.

We would like to keep the design in 1024x768 to make it easily view-able on all devices.

Regarding navigation there should only be a few sub-pages, like "Granite Slabs", "Granite Tiles", "Delivery", "Contact"

Aside from that we are open to designs. One idea we did have was to personalize the site and have a person there somehow to represent the company, making the user feel there are real people behind this site. This is just an idea and not a must.

The name of the company and site is "Silver Brook Petrano"

Thanks
Updates

Hello All,

Thanks for the great designs. There are some good looking designs that show beautiful kitchens but this site is made for the granite installers and not the retail consumers. So in order not to to confuse the buyers I would like to keep this as much about the raw products as possible. The raw products being the granite slabs, thereby making it obvious we don't sell granite counter tops. 

This design will really be the identity of this company so it is important we get the right message across on this index page and that this page is as complete as possible.

Again, thanks for all the work being put into this.

Target Market(s)

The target audience is granite installers or companies that would with granite slabs.

Industry/Entity Type

Business

```html
<!DOCTYPE html>
<html lang="en">
<head>
<meta charset="utf-8">
<title>Silver Brook Petrano – Black Granite Slabs and Tiles</title>
<link rel="stylesheet" href="https://fonts.googleapis.com/css2?family=Carrois+Gothic&family=Roboto:wght@300;400&family=Arimo:wght@400&display=swap">
<style>
  :root{
    --ink:#1b1b1b;
    --charcoal:#3d3c41;
    --band:#3e3d42;
    --card-bg:#efefef;
    --paper:#ffffff;
    --accent:#3c5a3a;
    --accent-dark:#3b5435;
    --line:#222222;
    --muted:#9a9a9a;
    --frame:#8a8a8a;
    --head-font:"Carrois Gothic", "Arial Narrow", sans-serif;
    --body-font:"Roboto", Arial, sans-serif;
    --plain-font:"Arimo", Arial, sans-serif;
  }
  *{box-sizing:border-box;margin:0;padding:0}
  html,body{width:895px;height:1200px;overflow:hidden;background:var(--paper)}
  .page{position:relative;width:895px;height:1200px;overflow:hidden;background:var(--paper);font-family:var(--body-font);color:var(--ink)}
  .abs{position:absolute}

  /* header */
  .site-header{left:0;top:0;width:895px;height:116px;background:linear-gradient(#dcdcdc,#f6f6f6 55%,#ffffff)}
  .phone{right:48px;top:27px;display:flex;align-items:center;gap:6px;font-family:var(--plain-font);font-size:19px;color:var(--ink)}
  .brand{left:339px;top:48px;width:200px;text-align:center;font-family:var(--head-font);font-size:17px;color:var(--ink);line-height:1}
  .brand small{display:block;font-size:8px;letter-spacing:1px;margin-top:3px}
  .brand-mark{left:429px;top:30px;width:16px;height:16px;background:var(--accent-dark)}
  .nav-rule{left:0;top:114px;width:895px;height:1px;background:var(--line)}
  .nav a{position:absolute;top:82px;font-family:var(--head-font);font-size:14.5px;color:var(--ink);text-decoration:none;letter-spacing:.3px}
  .diamond{position:absolute;top:110px;width:8px;height:8px;background:var(--line);transform:rotate(45deg)}

  /* hero */
  .hero-band{left:0;top:269px;width:895px;height:327px;background:var(--band);border-bottom:2px solid #8f8f8f}
  .hero-photo{left:37px;top:139px;width:821px;height:307px;border:2px solid var(--frame);background:linear-gradient(180deg,#d9d4c9 0%,#c9c3b6 42%,#2c2a2c 62%,#111 100%)}
  .slider-dots{left:371px;top:437px;width:97px;height:19px;border-radius:10px;background:var(--accent);display:flex;justify-content:center;align-items:center;gap:6px}
  .slider-dots span{width:7px;height:7px;border-radius:50%;background:#fff}
  .slider-dots span.off{background:#b9c3b6}
  .intro{left:45px;top:478px;width:805px;text-align:center;color:#fff}
  .intro h1{font-family:var(--head-font);font-weight:400;font-size:26px;line-height:1.2}
  .intro h1 .lead{font-size:21px}
  .intro p{font-weight:300;font-size:12.5px;line-height:18.8px;margin-top:4px}

  /* product cards */
  .card{width:357px;height:267px;background:var(--card-bg);box-shadow:0 8px 6px -4px rgba(0,0,0,.55)}
  .card h2{height:41px;background:var(--charcoal);color:#fff;font-family:var(--head-font);font-weight:400;font-size:21px;line-height:41px;padding-left:13px}
  .card .photo{height:134px}
  .card p{font-weight:300;font-size:11px;line-height:13.5px;padding:20px 12px 0 12px;color:#333}
  .card .more{position:absolute;right:31px;bottom:16px;font-family:var(--head-font);font-size:14px;color:var(--accent-dark);display:flex;align-items:center;gap:5px;text-decoration:none}
  .slab-photo{background:linear-gradient(160deg,#a9a9a7 0%,#1e1e24 35%,#15151a 70%,#8c8c88 100%)}
  .tile-photo{background:linear-gradient(180deg,#111116 0%,#0c0c10 85%,#8e8e8c 100%)}

  /* contact */
  .touch-title{left:28px;top:919px;font-family:var(--head-font);font-size:21.5px;color:var(--ink)}
  .touch-rule{left:30px;top:952px;width:789px;height:3px;background:var(--line)}
  .field{border:1px solid #b5b5b5;background:#fff;font-family:var(--plain-font);font-size:11px;color:#aaa;padding:5px 6px}
  .send{left:452px;top:1053px;width:56px;height:24px;background:#5b5b5b;color:#fff;font-family:var(--plain-font);font-size:14px;text-align:center;line-height:24px;box-shadow:-2px -2px 0 #d0d0d0}
  .divider{left:571px;top:971px;width:1px;height:123px;background:#9e9e9e}
  .address{left:602px;top:978px;width:205px;font-family:var(--plain-font);font-size:11.5px;line-height:14.8px;color:var(--ink)}
  .address h3{font-family:var(--head-font);font-weight:400;font-size:17.5px;margin-bottom:4px}
  .address p{text-align:justify}

  /* footer */
  .site-footer{left:0;top:1104px;width:895px;height:96px;background:var(--charcoal)}
  .social{top:14px;width:28px;height:28px;background:#e9e9e9;border:2px solid #999}
  .copyright{left:37px;top:69px;font-family:var(--plain-font);font-size:9.5px;color:#fff}
  .footer-brand{left:728px;top:56px;width:120px;text-align:center;font-family:var(--head-font);font-size:12px;color:#fff;line-height:1}
  .footer-mark{left:780px;top:30px;width:16px;height:16px;background:#fff}
  .footer-edge{left:857px;top:14px;width:1px;height:70px;background:#55545a}
</style>
</head>
<body>
<div class="page">

  <header class="site-header abs"></header>
  <div class="phone abs">
    <svg width="22" height="18" viewBox="0 0 22 18" aria-hidden="true">
      <path d="M2 6c0-3 4-5 9-5s9 2 9 5l-1 2h-4l-1-3H8L7 8H3z" fill="#1b1b1b"/>
      <rect x="5" y="9" width="12" height="8" rx="1.5" fill="#1b1b1b"/>
      <circle cx="11" cy="13" r="2.2" fill="#f3f3f3"/>
    </svg>
    <span>415 555 0192</span>
  </div>
  <div class="brand-mark abs"></div>
  <div class="brand abs">SILVER BROOK PETRANO<small>PORTO CLARO</small></div>

  <nav class="nav">
    <a style="left:43px">GRANITE SLABS</a>
    <a style="left:213px">GRANITE TILES</a>
    <a style="left:572px">DELIVERY</a>
    <a style="left:714px">CONTACT</a>
  </nav>
  <div class="nav-rule abs"></div>
  <span class="diamond" style="left:77px"></span>
  <span class="diamond" style="left:242px"></span>
  <span class="diamond" style="left:596px"></span>
  <span class="diamond" style="left:741px"></span>

  <section class="hero-band abs"></section>
  <div class="hero-photo abs" role="img" aria-label="Bright dining room with a polished black granite tile floor, table, chairs and upholstered bench"></div>
  <div class="slider-dots abs"><span></span><span></span><span></span><span class="off"></span></div>
  <div class="intro abs">
    <h1><span class="lead">We are suppliers of</span> Black Granite Slab and Black Granite Tiles</h1>
    <p>Lorem ipsum dolor sit amet cons ectetuer adipiscing elit praesent vestibulu moles lacus aenean nonummy.Lorem ipsum dolor sit amet cons ectetuer adipiscing elit praesent vestibulu moles lacus aenean nonummy.Lorem ipsum dolor sit amet cons ectetuer adip-iscing elit praesent vestibulu moles lacus aenean nonummy.</p>
  </div>

  <article class="card abs" style="left:59px;top:622px">
    <h2>GRANITE SLAB</h2>
    <div class="photo slab-photo" role="img" aria-label="Stack of polished black granite slabs"></div>
    <p>Lorem ipsum dolor sit amet cons ectetuer adipiscing elit praesent vestibulu moles lacus aenean nonummy.</p>
    <a class="more">MORE
      <svg width="13" height="9" viewBox="0 0 13 9" aria-hidden="true"><path d="M0 4.5h11M7.5 1l3.5 3.5L7.5 8" stroke="#3b5435" stroke-width="1.8" fill="none"/></svg>
    </a>
  </article>

  <article class="card abs" style="left:471px;top:623px">
    <h2>GRANITE TILE</h2>
    <div class="photo tile-photo" role="img" aria-label="Laid black granite floor tiles with sparkling flecks"></div>
    <p>Lorem ipsum dolor sit amet cons ectetuer adipiscing elit praesent vestibulu moles lacus aenean nonummy.</p>
    <a class="more">MORE
      <svg width="13" height="9" viewBox="0 0 13 9" aria-hidden="true"><path d="M0 4.5h11M7.5 1l3.5 3.5L7.5 8" stroke="#3b5435" stroke-width="1.8" fill="none"/></svg>
    </a>
  </article>

  <h2 class="touch-title abs" style="font-weight:400">Get in touch</h2>
  <div class="touch-rule abs"></div>
  <div class="field abs" style="left:35px;top:981px;width:233px;height:23px">Name</div>
  <div class="field abs" style="left:35px;top:1018px;width:233px;height:23px">Email</div>
  <div class="field abs" style="left:281px;top:984px;width:233px;height:57px">Message</div>
  <div class="send abs">Send</div>
  <div class="divider abs"></div>
  <address class="address abs" style="font-style:normal">
    <h3>Silver Brook Petrano</h3>
    <p>Bloco Norte, Sala 12, Rua das Pedras 40, Lagoa Azul, Porto Claro, PC, CEP-54321-000</p>
    <p style="margin-top:6px">Phone: 415 555 0192<br>Email: hello@petrano-stone.com</p>
  </address>

  <footer class="site-footer abs">
    <span class="social abs" style="left:37px" aria-label="Social profile"></span>
    <span class="social abs" style="left:73px" aria-label="Social profile"></span>
    <p class="copyright abs">Copyright 2013 Silver Brook Petrano. All right reserved.</p>
    <div class="footer-mark abs"></div>
    <div class="footer-brand abs">SILVER BROOK PETRANO</div>
    <div class="footer-edge abs"></div>
  </footer>

</div>
</body>
</html>
```